KTR Business Cards

We require business cards for our business. We would like a matte black back to the card, with our logo centred in the middle. The front side of the card is open to design.

Target Market(s)

Clients looking for legal services (professional)

Industry/Entity Type

Legal

Contact Information for Business Card

Dario Velkenor
Partner
Mobile: 0471 386 524
Email: dario@ktrlaw.co
Website: www.ktrlaw.co
Level 3, 118 Pembury Street
Sydney NSW 2000

Font styles to use
Other font styles liked:
• Avenir

Colors
f04a50
ffffff
1b1b1b

Requirements
Must have
• Black back with logo included in the centre of the card.
• Our font is Avenir.

```html
<!DOCTYPE html>
<html lang="en">
<head>
<meta charset="utf-8">
<title>KTR Legal – Business Card</title>
<link rel="stylesheet" href="https://fonts.googleapis.com/css2?family=Roboto:wght@400;500;700&display=swap">
<style>
  :root {
    --page-bg: #ecebea;
    --card-black: #231f20;
    --brand-red: #d1234a;
    --brand-red-deep: #a51b3b;
    --text-white: #ffffff;
    --text-soft: #e4e4e4;
  }
  * { box-sizing: border-box; margin: 0; padding: 0; }
  html, body {
    width: 1200px; height: 900px; overflow: hidden;
    background: var(--page-bg);
    font-family: "Roboto", Arial, sans-serif;
  }
  .business-card {
    position: absolute; left: 160px; top: 178px;
    width: 880px; height: 543px;
    background: var(--card-black);
    box-shadow: 0 14px 40px rgba(0,0,0,.25);
    overflow: hidden;
  }
  .accent-panel {
    position: absolute; inset: 0;
    background: linear-gradient(180deg, var(--brand-red) 0%, var(--brand-red-deep) 100%);
    clip-path: polygon(0 0, 241px 0, 536px 295px, 302px 543px, 0 543px);
  }
  .firm-name {
    position: absolute; right: 36px; top: 86px;
    display: flex; align-items: center; gap: 16px;
    color: var(--text-white);
    font-weight: 500; font-size: 32px; letter-spacing: .5px;
  }
  .firm-mark {
    width: 22px; height: 22px; background: var(--brand-red);
  }
  .contact-block {
    position: absolute; right: 36px; top: 254px;
    text-align: right; color: var(--text-soft);
  }
  .person-name {
    color: var(--brand-red); font-weight: 700;
    font-size: 30px; letter-spacing: .5px; line-height: 1.1;
  }
  .person-role { font-size: 23px; margin-top: 4px; }
  .contact-list { list-style: none; margin-top: 20px; font-size: 23px; line-height: 33px; }
  .contact-list li { display: flex; justify-content: flex-end; align-items: center; gap: 4px; }
  .contact-icon { width: 17px; height: 17px; fill: var(--brand-red); }
  .office-address { font-style: normal; font-size: 23px; line-height: 33px; margin-top: 10px; }
</style>
</head>
<body>
  <div class="business-card">
    <div class="accent-panel" role="img" aria-label="Red brand panel with large decorative logo mark"></div>

    <div class="firm-name"><span class="firm-mark"></span>KTR LEGAL</div>

    <div class="contact-block">
      <p class="person-name">DARIO VELKENOR</p>
      <p class="person-role">Partner</p>
      <ul class="contact-list">
        <li>0471 386 524
          <svg class="contact-icon" viewBox="0 0 16 16" aria-hidden="true"><path d="M2 5c0-2 2-3 6-3s6 1 6 3v1h-3V5H5v1H2zM4 7h8l2 7H2z"/></svg>
        </li>
        <li>dario@ktrlaw.co
          <svg class="contact-icon" viewBox="0 0 16 16" aria-hidden="true"><path d="M1 3h14v10H1zM2 4.5v.6l6 4 6-4v-.6z" fill-rule="evenodd"/></svg>
        </li>
        <li>www.ktrlaw.co
          <svg class="contact-icon" viewBox="0 0 16 16" aria-hidden="true"><circle cx="8" cy="8" r="7"/><path d="M4 6c2-1 3 1 2 2s1 3 2 4M10 3c-1 2 1 3 3 3" stroke="#231f20" stroke-width="1.2" fill="none"/></svg>
        </li>
      </ul>
      <address class="office-address">Level 3, 118 Pembury<br>Street, Sydney NSW 2000</address>
    </div>
  </div>
</body>
</html>
```